I have an animal hospital. I want a poster to hang in each exam room to show a picture of a normal sized heart and then an enlarged heart of a dog that was fed a grain-free diet. I want to warn people not to feed grain-free diets. Maybe at the top of the poster, "Do you feed grain-free?" and then the x-ray comparison, then the warnings of Canine Dilated Cardiomyopathy.

```html
<!DOCTYPE html>
<html lang="en">
<head>
<meta charset="utf-8">
<title>Do You Feed Grain-Free? – Exam Room Poster</title>
<link rel="stylesheet" href="https://fonts.googleapis.com/css2?family=Luckiest+Guy&family=Poppins:wght@500;600;700&display=swap">
<style>
  :root {
    --page-bg: #e6e6e6;
    --yellow-deep: #f7b90f;
    --yellow-light: #fcd65a;
    --brown: #7a3d08;
    --ink: #111111;
    --white: #ffffff;
    --xray-dark: #0b0b0b;
    --xray-light: #cfcfcf;
  }
  * { margin: 0; padding: 0; box-sizing: border-box; }
  html, body {
    width: 1200px; height: 2588px; overflow: hidden;
    background: var(--page-bg);
  }
  .poster {
    position: absolute; left: 50px; top: 469px;
    width: 1024px; height: 1536px;
    transform: scale(1.0742); transform-origin: top left;
    background: radial-gradient(ellipse at 50% 55%, var(--yellow-light) 0%, var(--yellow-deep) 75%);
    box-shadow: 0 6px 18px rgba(0,0,0,0.25);
    overflow: hidden;
    font-family: "Poppins", sans-serif;
  }
  .headline-kicker {
    position: absolute; top: 52px; left: 0; width: 100%;
    text-align: center;
    font-family: "Luckiest Guy", cursive;
    font-size: 60px; letter-spacing: 2px;
    color: var(--white);
    -webkit-text-stroke: 3px var(--brown);
    paint-order: stroke fill;
  }
  .headline-main {
    position: absolute; top: 118px; left: 0; width: 100%;
    text-align: center;
    font-family: "Luckiest Guy", cursive;
    font-size: 118px; letter-spacing: 2px;
    color: var(--brown);
  }
  .comparison-art { position: absolute; left: 0; top: 260px; }
  .xray {
    position: absolute; border-radius: 50%;
    background: radial-gradient(ellipse at 50% 55%, var(--xray-light) 0%, #7c7c7c 35%, #2a2a2a 62%, var(--xray-dark) 80%);
  }
  .xray--normal { left: 124px; top: 296px; width: 344px; height: 344px; border: 3px solid var(--brown); }
  .xray--enlarged { left: 567px; top: 292px; width: 330px; height: 330px;
    background: radial-gradient(ellipse at 50% 60%, #dcdcdc 0%, #8a8a8a 45%, #2a2a2a 70%, var(--xray-dark) 85%); }
  .warnings-title {
    position: absolute; top: 700px; left: 0; width: 100%;
    text-align: center; font-weight: 700; font-size: 42px; line-height: 50px;
    color: var(--ink);
  }
  .warnings-subtitle {
    position: absolute; top: 752px; left: 0; width: 100%;
    display: flex; align-items: center; gap: 16px;
    font-weight: 700; font-size: 42px; line-height: 52px; color: var(--brown);
  }
  .warnings-subtitle::before, .warnings-subtitle::after {
    content: ""; flex: 1; height: 3px; background: var(--brown);
  }
  .symptom-list { position: absolute; list-style: none; }
  .symptom-list--left { left: 152px; top: 836px; width: 400px; }
  .symptom-list--right { left: 576px; top: 836px; width: 420px; }
  .symptom {
    position: relative; padding-left: 52px;
    font-weight: 500; font-size: 23px; line-height: 25.5px; color: var(--ink);
  }
  .symptom-list--left .symptom { margin-bottom: 26px; }
  .symptom-list--right .symptom { margin-bottom: 25px; }
  .symptom-list--right .symptom.tight { margin-bottom: 25px; }
  .symptom .paw { position: absolute; left: 0; top: 0; width: 28px; height: 26px; }
  .puppy-strip { position: absolute; left: 0; top: 1150px; }
</style>
</head>
<body>
<svg width="0" height="0" style="position:absolute">
  <symbol id="paw" viewBox="0 0 28 26">
    <ellipse cx="14" cy="18" rx="7.5" ry="6.5" fill="#111"/>
    <ellipse cx="5" cy="10" rx="3.3" ry="4" fill="#111"/>
    <ellipse cx="10.5" cy="5" rx="3.3" ry="4" fill="#111"/>
    <ellipse cx="17.5" cy="5" rx="3.3" ry="4" fill="#111"/>
    <ellipse cx="23" cy="10" rx="3.3" ry="4" fill="#111"/>
  </symbol>
</svg>

<main class="poster">
  <h1 class="headline-kicker">DO YOU FEED</h1>
  <h2 class="headline-main">GRAIN-FREE?</h2>

  <svg class="comparison-art" width="1024" height="400" viewBox="0 0 1024 400">
    <defs>
      <path id="arc-left" d="M167.4 361.2 A200 200 0 0 1 211.5 26.7"/>
      <path id="arc-right" d="M827 32.5 A190 190 0 0 1 827 361.5"/>
    </defs>
    <path class="after-band" d="M1024 13 H732 A184 184 0 0 0 732 381 H1024 Z" fill="var(--brown)"/>
    <path class="normal-arc" d="M376.3 35.8 A190 190 0 0 1 391 372.5" fill="none" stroke="var(--brown)" stroke-width="5"/>
    <text font-family="Poppins, sans-serif" font-weight="700" font-size="30" fill="var(--brown)" letter-spacing="1">
      <textPath href="#arc-left" startOffset="40">WITH GRAIN DIET</textPath>
    </text>
    <text font-family="Poppins, sans-serif" font-weight="700" font-size="27" fill="var(--white)" letter-spacing="1">
      <textPath href="#arc-right" startOffset="0">AFTER GRAIN FREE DIET</textPath>
    </text>
  </svg>

  <div class="xray xray--normal" role="img" aria-label="Chest x-ray of a dog with a normal sized heart, fed a grain diet"></div>
  <div class="xray xray--enlarged" role="img" aria-label="Chest x-ray of a dog with an enlarged heart after a grain-free diet"></div>

  <p class="warnings-title">The warnings of</p>
  <p class="warnings-subtitle">Canine Dilated Cardiomyopathy</p>

  <ul class="symptom-list symptom-list--left">
    <li class="symptom"><svg class="paw"><use href="#paw"/></svg>Rapid breathing when resting or sleeping (more than 30-35 breaths per minute).</li>
    <li class="symptom"><svg class="paw"><use href="#paw"/></svg>Increased effort associated with breathing.</li>
    <li class="symptom"><svg class="paw"><use href="#paw"/></svg>Restless sleeping; moving around a lot and changing positions.</li>
  </ul>
  <ul class="symptom-list symptom-list--right">
    <li class="symptom"><svg class="paw"><use href="#paw"/></svg>Coughing or gagging.</li>
    <li class="symptom"><svg class="paw"><use href="#paw"/></svg>Weakness.</li>
    <li class="symptom"><svg class="paw"><use href="#paw"/></svg>Reduced ability to exercise.</li>
    <li class="symptom"><svg class="paw"><use href="#paw"/></svg>Fainting spells.</li>
    <li class="symptom"><svg class="paw"><use href="#paw"/></svg>Difficulty breathing</li>
  </ul>

  <svg class="puppy-strip" width="1024" height="386" viewBox="0 0 1024 386" role="img" aria-label="Row of five puppies: a chocolate retriever, a terrier, a bulldog, a pug and a beagle">
    <defs>
      <linearGradient id="puppy-tones" x1="0" y1="0" x2="1" y2="0">
        <stop offset="0" stop-color="#4a2a1c"/>
        <stop offset="0.3" stop-color="#e9e2d8"/>
        <stop offset="0.5" stop-color="#efe6de"/>
        <stop offset="0.7" stop-color="#b89870"/>
        <stop offset="1" stop-color="#8a5a36"/>
      </linearGradient>
    </defs>
    <path d="M0 140 Q70 100 140 100 L150 55 Q260 10 420 30 Q480 36 520 62 Q600 52 645 105 L700 165 Q790 150 830 170 Q900 95 1024 112 V386 H0 Z" fill="var(--white)"/>
    <path d="M0 150 Q72 112 146 110 L158 66 Q262 22 416 40 Q476 46 518 74 Q596 64 636 114 L694 176 Q788 162 834 182 Q902 106 1024 122 V386 H0 Z" fill="url(#puppy-tones)"/>
  </svg>
</main>
</body>
</html>
```